Bookmark Design

We would like to design a book mark with logos of our two business and a quote.

One side with the quote "The first wealth is health" - Tobias Quill Harrow and the two logos.

The back side has the two logos with its respective phone numbers and a common address (this is to be advised to the winner of the project).

```html
<!DOCTYPE html>
<html lang="en">
<head>
<meta charset="utf-8">
<title>Bookmark Design – Harbourline Dental &amp; Greenvale Clinic</title>
<link rel="stylesheet" href="https://fonts.googleapis.com/css2?family=Ubuntu:wght@400;500;700&family=Bevan&family=Yellowtail&display=swap">
<style>
  :root {
    --page: #ffffff;
    --frame-top: #7a8cb2;
    --frame-bottom: #cfd8e3;
    --front-top: #b9d6ea;
    --front-bottom: #f3f8f2;
    --back-top: #aecadd;
    --back-mid: #ffffff;
    --back-bottom: #e3f1e4;
    --shadow: #e8ebef;
    --ink: #4a4f57;
    --ink-soft: #5a5f66;
    --script-blue: #3b63a8;
    --green: #5fb35f;
    --blue: #1f56a8;
    --rule: #b8bcc2;
  }
  * { box-sizing: border-box; margin: 0; padding: 0; }
  html, body { width: 1200px; height: 849px; overflow: hidden; background: var(--page); }
  .canvas { position: relative; width: 1200px; height: 849px; font-family: "Ubuntu", sans-serif; }

  .bookmark { position: absolute; top: 116px; width: 205px; height: 612px; }
  .bookmark--front { left: 312px; }
  .bookmark--back { left: 675px; }
  .bookmark__shape { position: absolute; inset: 0; overflow: visible; }
  .bookmark__content { position: absolute; inset: 0; text-align: center; }

  .dots { position: absolute; left: 0; right: 0; display: flex; justify-content: center; align-items: center; gap: 8px; }
  .dots span { width: 4px; height: 4px; border-radius: 50%; background: #fff; }
  .dots span.dash { width: 5px; height: 1.5px; border-radius: 1px; }

  .quote__caps { position: absolute; left: 0; right: 0; font-family: "Bevan", serif; color: #6d7a86;
    text-shadow: 1px 1px 0 #3e4b57; letter-spacing: .5px; }
  .quote__first { top: 106px; font-size: 23px; }
  .quote__is { top: 192px; font-size: 20px; }
  .quote__script { position: absolute; left: 0; right: 0; font-family: "Yellowtail", cursive; color: var(--script-blue);
    text-shadow: 2px 2px 0 #9aa3ad; font-size: 50px; line-height: 1; }
  .quote__wealth { top: 136px; }
  .quote__health { top: 224px; }
  .quote__author { position: absolute; top: 300px; left: 0; right: 0; font-size: 9px; color: var(--ink); letter-spacing: .2px; }

  .brand { position: absolute; left: 0; right: 0; display: flex; align-items: center; justify-content: center; gap: 7px;
    font-family: "Ubuntu", sans-serif; font-weight: 700; line-height: 1.05; text-align: left; }
  .brand__dot { flex: none; border-radius: 50%; }
  .brand--dental { color: var(--green); font-size: 21px; }
  .brand--dental .brand__dot { width: 22px; height: 22px; background: var(--green); }
  .brand--clinic { color: var(--blue); font-size: 20px; }
  .brand--clinic .brand__dot { width: 22px; height: 22px; background: var(--blue); }

  .contact__phone { position: absolute; left: 40px; right: 40px; font-size: 11px; font-weight: 500; color: var(--ink);
    padding-bottom: 3px; border-bottom: 1px dashed var(--rule); white-space: nowrap; }
  .contact__address { position: absolute; top: 455px; left: 10px; right: 10px; font-size: 11px; font-weight: 500;
    color: var(--ink); line-height: 1.25; }
</style>
</head>
<body>
<main class="canvas">

  <!-- Front side -->
  <article class="bookmark bookmark--front">
    <svg class="bookmark__shape" viewBox="0 0 205 612" aria-hidden="true">
      <defs>
        <linearGradient id="frame-front" x1="0" y1="0" x2="0" y2="1">
          <stop offset="0" stop-color="var(--frame-top)"/>
          <stop offset="1" stop-color="var(--frame-bottom)"/>
        </linearGradient>
        <linearGradient id="panel-front" x1="0" y1="0" x2="0" y2="1">
          <stop offset="0" stop-color="var(--front-top)"/>
          <stop offset="1" stop-color="var(--front-bottom)"/>
        </linearGradient>
      </defs>
      <path d="M105 5 L203 72 Q208 76 208 84 L208 603 Q208 615 196 615 L15 615 Q3 615 3 603 L3 84 Z" fill="var(--shadow)"/>
      <path d="M102.5 2 L200 68 Q205 72 205 80 L205 600 Q205 612 193 612 L12 612 Q0 612 0 600 L0 80 Q0 72 5 68 Z"
            fill="url(#frame-front)" stroke="url(#frame-front)" stroke-width="3" stroke-linejoin="round"/>
      <path d="M102.5 14 L189 72 Q194 76 194 84 L194 594 Q194 601 187 601 L18 601 Q11 601 11 594 L11 84 Q11 76 16 72 Z"
            fill="url(#panel-front)" stroke="url(#panel-front)" stroke-width="3" stroke-linejoin="round"/>
      <circle cx="102.5" cy="32" r="8" fill="#fff"/>
    </svg>
    <div class="bookmark__content">
      <div class="dots" style="top:79px"><span class="dash"></span><span></span><span></span><span></span><span class="dash"></span></div>
      <p class="quote__caps quote__first">THE FIRST</p>
      <p class="quote__script quote__wealth">Wealth</p>
      <p class="quote__caps quote__is">IS</p>
      <p class="quote__script quote__health">Health</p>
      <p class="quote__author">- TOBIAS QUILL HARROW -</p>
      <div class="dots" style="top:337px"><span class="dash"></span><span></span><span></span><span></span><span class="dash"></span></div>
      <div class="brand brand--dental" style="top:398px"><span class="brand__dot"></span><span>Harbourline<br>Dental</span></div>
      <div class="brand brand--clinic" style="top:506px"><span class="brand__dot"></span><span>Greenvale<br>Clinic</span></div>
    </div>
  </article>

  <!-- Back side -->
  <article class="bookmark bookmark--back">
    <svg class="bookmark__shape" viewBox="0 0 205 612" aria-hidden="true">
      <defs>
        <linearGradient id="frame-back" x1="0" y1="0" x2="0" y2="1">
          <stop offset="0" stop-color="var(--frame-top)"/>
          <stop offset="1" stop-color="var(--frame-bottom)"/>
        </linearGradient>
        <linearGradient id="panel-back" x1="0" y1="0" x2="0" y2="1">
          <stop offset="0" stop-color="var(--back-top)"/>
          <stop offset=".1" stop-color="var(--back-top)"/>
          <stop offset=".24" stop-color="var(--back-mid)"/>
          <stop offset=".82" stop-color="var(--back-mid)"/>
          <stop offset="1" stop-color="var(--back-bottom)"/>
        </linearGradient>
      </defs>
      <path d="M105 5 L203 72 Q208 76 208 84 L208 603 Q208 615 196 615 L15 615 Q3 615 3 603 L3 84 Z" fill="var(--shadow)"/>
      <path d="M102.5 2 L200 68 Q205 72 205 80 L205 600 Q205 612 193 612 L12 612 Q0 612 0 600 L0 80 Q0 72 5 68 Z"
            fill="url(#frame-back)" stroke="url(#frame-back)" stroke-width="3" stroke-linejoin="round"/>
      <path d="M102.5 14 L189 72 Q194 76 194 84 L194 594 Q194 601 187 601 L18 601 Q11 601 11 594 L11 84 Q11 76 16 72 Z"
            fill="url(#panel-back)" stroke="url(#panel-back)" stroke-width="3" stroke-linejoin="round"/>
      <circle cx="102.5" cy="32" r="8" fill="#fff"/>
    </svg>
    <div class="bookmark__content">
      <div class="brand brand--dental" style="top:176px"><span class="brand__dot"></span><span>Harbourline<br>Dental</span></div>
      <p class="contact__phone" style="top:246px">Phone#: (02) 5550-1842</p>
      <div class="brand brand--clinic" style="top:316px"><span class="brand__dot"></span><span>Greenvale<br>Clinic</span></div>
      <p class="contact__phone" style="top:400px">Phone#: (02) 5550-1842</p>
      <p class="contact__address">Adress:<br>18 Willow Crescent<br>BELLMORE, New South<br>Wales(NSW), 2600</p>
    </div>
  </article>

</main>
</body>
</html>
```